TV - business card

Tidewell Vantage is an insurance brokerage firm, inovative, proactive, vigorous, which aims to become the leader of the insurance brokers in Anfrica. We should like to get some designs which should be avoided also in Gray / Metallic for the Administration and Orange / Blue for the Managers (ike in the picture sent). The Blue / Green logo is not the correct one, but the source of the file. Please adjust the color accordingly for the business cards. 1 / Orange / Blue 2 / Gray / Metallic We want something classic but which is transmitted strenght, inovation, modernity and most of all, rapidity. We want something start-up like, very punchy and catching eye remaining profesional at the same time. Name: Delton Ashgrove Function: Managing Director Address: N ° 73/74 Cmt. Bolembe - R / C 2B Esquerda - Bairro Quimbuta - Luanda Tel: (+244) 947 385 619 Email: delton.ashgrove@tidewell-v.com Website: www.tidewell-v. com We want classic in the front and creative, colorfull at the back. The cards will be printed in relief, with very high quality of paper.
Industry/Entity Type
Insurance Broker
Colors
Designer to choose colors to be used in the design.
Look and feel

```html
<!DOCTYPE html>
<html lang="en">
<head>
<meta charset="utf-8">
<title>Tidewell Vantage – Business Card</title>
<link href="https://fonts.googleapis.com/css2?family=Merriweather:wght@700&family=Open+Sans:wght@400;600;700&display=swap" rel="stylesheet">
<style>
  :root {
    --canvas: #e6e3df;
    --card: #050505;
    --gold: #e2bd1f;
    --gold-deep: #b8900c;
    --silver: #a7a8ab;
    --white: #ffffff;
    --rule: #8c8c8c;
  }
  * { margin: 0; padding: 0; box-sizing: border-box; }
  html, body { width: 1200px; height: 900px; overflow: hidden; }
  body {
    background: var(--canvas);
    font-family: "Open Sans", sans-serif;
    position: relative;
  }
  .card {
    position: absolute;
    left: 250px;
    width: 700px;
    height: 400px;
    background: var(--card);
    color: var(--white);
    box-shadow: 0 6px 18px rgba(0,0,0,.25);
    overflow: hidden;
  }
  .card--details { top: 40px; }
  .card--brand { top: 470px; }

  /* details side */
  .brand {
    position: absolute;
    display: flex;
    align-items: center;
    gap: 14px;
  }
  .brand__mark {
    border-radius: 50%;
    border: 6px solid var(--silver);
    flex: none;
  }
  .brand__name {
    font-family: "Open Sans", sans-serif;
    font-weight: 700;
    color: var(--gold);
    text-transform: uppercase;
    letter-spacing: 1px;
    white-space: nowrap;
  }
  .card--details .brand { left: 48px; top: 110px; }
  .card--details .brand__mark { width: 84px; height: 84px; }
  .card--details .brand__name { font-size: 30px; }

  .holder {
    position: absolute;
    right: 44px;
    top: 52px;
    display: flex;
    align-items: center;
    gap: 14px;
  }
  .holder__icon { width: 40px; height: 40px; }
  .holder__text { text-align: right; }
  .holder__name {
    font-family: "Merriweather", serif;
    font-weight: 700;
    font-size: 24px;
    color: var(--gold);
    line-height: 1.1;
  }
  .holder__role { font-size: 15px; color: var(--silver); }

  .contacts {
    position: absolute;
    left: 380px;
    top: 196px;
    list-style: none;
    font-size: 15px;
  }
  .contacts li { display: flex; align-items: center; gap: 10px; height: 24px; }
  .contacts svg { width: 16px; height: 16px; flex: none; }

  .gold-rule {
    position: absolute;
    left: 0; right: 0;
    top: 276px;
    height: 3px;
    background: linear-gradient(90deg, var(--gold-deep), var(--gold) 50%, var(--gold-deep));
  }
  .address {
    position: absolute;
    left: 48px;
    top: 296px;
    display: flex;
    gap: 12px;
    font-size: 16px;
    line-height: 1.35;
  }
  .address svg { width: 20px; height: 26px; flex: none; margin-top: 4px; }

  .edge-line {
    position: absolute;
    left: 0; right: 0;
    height: 1px;
    background: var(--rule);
    opacity: .6;
  }
  .edge-line--top { top: 14px; }
  .edge-line--bottom { bottom: 14px; }

  /* brand side */
  .card--brand .brand {
    left: 0; right: 0;
    top: 96px;
    flex-direction: column;
    gap: 22px;
  }
  .card--brand .brand__mark { width: 150px; height: 150px; border-width: 10px; }
  .card--brand .brand__name { font-size: 50px; letter-spacing: 2px; }
  .website {
    position: absolute;
    left: 0; right: 0;
    top: 322px;
    text-align: center;
    font-weight: 700;
    font-size: 24px;
    letter-spacing: 14px;
    color: var(--white);
  }
</style>
</head>
<body>

<section class="card card--details">
  <div class="edge-line edge-line--top"></div>

  <div class="brand">
    <span class="brand__mark"></span>
    <span class="brand__name">Tidewell Vantage</span>
  </div>

  <div class="holder">
    <svg class="holder__icon" viewBox="0 0 40 40" aria-hidden="true">
      <circle cx="20" cy="20" r="20" fill="#fff"/>
      <circle cx="20" cy="15" r="6" fill="none" stroke="#050505" stroke-width="2.5"/>
      <path d="M9 32c2-7 20-7 22 0" fill="none" stroke="#050505" stroke-width="2.5"/>
    </svg>
    <div class="holder__text">
      <p class="holder__name">Delton Ashgrove</p>
      <p class="holder__role">Managing Director</p>
    </div>
  </div>

  <ul class="contacts">
    <li>
      <svg viewBox="0 0 16 16" aria-hidden="true"><path d="M3 1l3 3-2 2c1 2 3 4 5 5l2-2 3 3-2 3C7 15 1 9 1 3z" fill="#a7a8ab"/></svg>
      (+244) 947 385 619
    </li>
    <li>
      <svg viewBox="0 0 16 16" aria-hidden="true"><rect x="1" y="3" width="14" height="10" fill="#a7a8ab"/><path d="M1 3l7 6 7-6" fill="none" stroke="#050505" stroke-width="1.4"/></svg>
      delton.ashgrove@tidewell-v.com
    </li>
    <li>
      <svg viewBox="0 0 16 16" aria-hidden="true"><circle cx="8" cy="8" r="6.5" fill="none" stroke="#a7a8ab" stroke-width="1.5"/><path d="M1.5 8h13M8 1.5c-3 3-3 10 0 13M8 1.5c3 3 3 10 0 13" fill="none" stroke="#a7a8ab" stroke-width="1.2"/></svg>
      www.tidewell-v.com
    </li>
  </ul>

  <div class="gold-rule"></div>

  <div class="address">
    <svg viewBox="0 0 20 26" aria-hidden="true"><path d="M10 0a9 9 0 0 1 9 9c0 7-9 17-9 17S1 16 1 9a9 9 0 0 1 9-9z" fill="#a7a8ab"/><circle cx="10" cy="9" r="3.5" fill="#050505"/></svg>
    <p>N ° 73/74 Cmt. Bolembe - R / C 2B Esquerda -<br>Bairro Quimbuta - Luanda</p>
  </div>

  <div class="edge-line edge-line--bottom"></div>
</section>

<section class="card card--brand">
  <div class="edge-line edge-line--top"></div>
  <div class="brand">
    <span class="brand__mark"></span>
    <span class="brand__name">Tidewell Vantage</span>
  </div>
  <p class="website">www.tidewell-v. com</p>
  <div class="edge-line edge-line--bottom"></div>
</section>

</body>
</html>
```